Hochzeitseinladung im Pocketfold-Style
Zielgruppe
Vertrieb von Hochzeitspapeterie. Unsere Zielgruppe ist weiblich, verlobt, 20 - 40 Jahre alt.
Aufgabenstellung
Wir benötigen ein Design für die Einladungskarte + Einleger in einen Pocketfoldumschlag (Umschlag soll nicht gestaltet werden).
EINLADUNGSTEXT
Formate in mm:130x130mm
Vorgabe für Design / Layout:
Schlichtes Design ohne aufwendige Grafiken mit leichtem Hauch zum Vintage ("Vintage Wedding Icons" z.B. Girlande, Zweig, Retro-Icons wie Vintage Fahrrad, Vogelkäfig, Lampions, etc).
Evtl. oben Initialen C und S unterbringen
Schrift: Farbe dunkelgrau, Font (nur lizenzfreie)
Keine Verwendung von Sonderfarben
Farben Dokument gesamt incl. Grafiken und Objekten: Max. 3 Farben (z.b. Mix aus Grau, Koralle, Altrosa, Mint)
Keine Fotos
EINLEGER
3 x Format in mm: 130x130mm
- Hier nur ein Design für die Überschrift passend zum Einladungsdesign
(3 Überschriften: Unser Tag + Hotel & Anreise + RSVP/Antwort)
Abnahme:
Designbeispiele als pdf zur Korrektur/Abnahme
Fertiges Design soll am Ende als InDesign File sowie als druckfähige pdf-Datei an Käufer gesendet werden.
Vom Gewinner-Design gehen alle Rechte zur kommerziellen Nutzung an den Käufer über.

```html
<!DOCTYPE html>
<html lang="de">
<head>
<meta charset="utf-8">
<title>Hochzeitseinladung – Clara &amp; Simon</title>
<link rel="stylesheet" href="https://fonts.googleapis.com/css2?family=Sofia&display=swap">
<style>
  :root {
    --backdrop: #e6e1dc;
    --paper: #f6f4ef;
    --ink: #2e2b2a;
    --band: #474341;
    --band-text: #e9e5e0;
    --rose-soft: #f3c6d4;
    --grey-soft: #d8d4cf;
  }
  * { box-sizing: border-box; margin: 0; padding: 0; }
  html, body {
    width: 1200px; height: 696px; overflow: hidden;
    background: var(--backdrop);
  }
  .invitation {
    position: absolute; left: 270px; top: 18px;
    width: 660px; height: 660px;
    background: var(--paper);
    box-shadow: 0 1px 3px rgba(0,0,0,.12);
    font-family: "Sofia", cursive;
    color: var(--ink);
    text-align: center;
  }
  .monogram {
    position: absolute; left: 260px; top: 18px;
    width: 140px; height: 200px;
    border-radius: 10px;
    background: radial-gradient(ellipse at center, var(--grey-soft) 0%, var(--paper) 75%);
  }
  .headline { position: absolute; left: 0; width: 100%; line-height: 1; }
  .headline--intro { top: 228px; font-size: 22px; }
  .headline--main  { top: 256px; font-size: 27px; }
  .headline--place { top: 292px; font-size: 20px; }
  .headline--date  { top: 320px; font-size: 18px; }

  .doodle {
    position: absolute; border-radius: 50%;
    background: radial-gradient(circle, var(--grey-soft) 0%, var(--paper) 72%);
  }
  .doodle--butterfly { left: 110px; top: 322px; width: 58px; height: 52px; }
  .doodle--heart { left: 500px; top: 328px; width: 46px; height: 42px; }

  .emblem {
    position: absolute; left: 284px; top: 358px;
    width: 92px; height: 102px; border-radius: 46px;
    background: radial-gradient(ellipse, var(--rose-soft) 0%, var(--paper) 78%);
  }
  .schedule {
    position: absolute; left: 0; top: 385px;
    width: 652px; height: 48px;
    background: var(--band);
    color: var(--band-text);
    font-size: 10px; line-height: 1.3; text-align: left;
  }
  .schedule__item { position: absolute; top: 7px; white-space: nowrap; }
  .schedule__item--ceremony { left: 150px; }
  .schedule__item--dinner { left: 388px; }
  .schedule__item .time { font-size: 11px; }
  .schedule__badge {
    position: absolute; left: 296px; top: 2px;
    width: 60px; height: 44px; border-radius: 22px;
    border: 1.5px solid var(--band-text);
    background: var(--band);
  }

  .greeting { position: absolute; top: 486px; left: 0; width: 100%; font-size: 11.5px; line-height: 1.6; }
  .rsvp { position: absolute; top: 528px; left: 0; width: 100%; font-size: 17px; }
  .contact { position: absolute; top: 562px; left: 0; width: 100%; font-size: 11px; line-height: 1.75; }
</style>
</head>
<body>
  <main class="invitation">
    <div class="monogram" role="img" aria-label="Handgeschriebener Schriftzug Clara &amp; Simon mit Save-the-Date-Banderole und Schnörkeln"></div>

    <p class="headline headline--intro">Come away with us</p>
    <p class="headline headline--main">to a Wedding Weekend</p>
    <p class="headline headline--place">in The Wolds, England</p>
    <p class="headline headline--date">09. Juli 2017/Sonntag</p>

    <div class="doodle doodle--butterfly" role="img" aria-label="Gezeichneter Schmetterling mit gestrichelter Flugbahn"></div>
    <div class="doodle doodle--heart" role="img" aria-label="Gezeichnetes Herz mit gestrichelter Flugbahn"></div>

    <div class="emblem" role="img" aria-label="Rosafarbenes Zierornament"></div>

    <section class="schedule">
      <div class="schedule__item schedule__item--ceremony">
        <span class="time">14.00 Zeremonie</span><br>The Ashgrove House<br>in Lower Brookfield
      </div>
      <div class="schedule__badge" role="img" aria-label="Blüten-Emblem"></div>
      <div class="schedule__item schedule__item--dinner">
        <span class="time">18.30 Restaurant/Hotel</span><br>The Linden<br>in Hollowmere
      </div>
    </section>

    <p class="greeting">Wir feiern unsere Hochzeit und möchten diesen<br>schönen Moment gerne mit Euch gemeinsam erleben.</p>
    <p class="rsvp">Antwort bitte bis 31.März</p>
    <p class="contact">Familie Beispielhof | Lindenweg 1 | 12345 Beispielstadt<br>familie@beispielhof.de | +49 123 987654</p>
  </main>
</body>
</html>
```